Location detection - billboard

Poster / billboard is to be hung in front of the building. When you see the billboard you have to know immediately that here is a location, which company, what we do, based on picture or text, website address.
The main business is professional window tinting. But we also make paint protection film.
It shouldn't be too full, legible but clear
There should be a billboard on the street so people know that there is a location. With logo, performance information and that people are welcome (maybe with a => (here) sign)
Colors should be similar to those on the uploaded images

Target Market(s)

Customers - motorists

Font styles to use
Sans Serif

Requirements
Must have
• My logo must be on it. It must be clear that there is a location here and how to reach us

```html
<!DOCTYPE html>
<html lang="de">
<head>
<meta charset="utf-8">
<title>Tintora Billboard</title>
<link rel="stylesheet" href="https://fonts.googleapis.com/css2?family=Anton&family=Exo+2:ital,wght@1,700;1,800&display=swap">
<style>
  :root {
    --page: #f2f2f2;
    --panel-grey: #3d3f41;
    --panel-black: #0d0d0e;
    --brand-red: #e32228;
    --headline: #e4e4e4;
    --white: #ffffff;
  }
  html, body {
    margin: 0;
    width: 1200px;
    height: 1200px;
    overflow: hidden;
    background: var(--page);
  }
  .canvas {
    position: relative;
    width: 1200px;
    height: 1200px;
  }
  .billboard {
    position: absolute;
    left: 40px;
    top: 435px;
    width: 1120px;
    height: 330px;
    filter: drop-shadow(0 6px 10px rgba(0,0,0,0.35));
  }
  .brand-name { font-family: "Anton", sans-serif; fill: var(--brand-red); }
  .tagline { font-family: "Exo 2", sans-serif; font-style: italic; font-weight: 700; fill: var(--white); }
  .headline { font-family: "Anton", sans-serif; fill: var(--headline); }
  .website { font-family: "Exo 2", sans-serif; font-style: italic; font-weight: 700; fill: var(--white); }
  .phone { font-family: "Exo 2", sans-serif; font-style: italic; font-weight: 800; fill: var(--panel-black); }
  .address { font-family: "Exo 2", sans-serif; font-style: italic; font-weight: 700; fill: var(--white); }
</style>
</head>
<body>
<main class="canvas">
  <svg class="billboard" viewBox="0 0 1390 410" xmlns="http://www.w3.org/2000/svg">
    <rect class="panel-black" width="1390" height="410" fill="var(--panel-black)"/>
    <path class="top-accent" d="M420,0 L1110,0 L480,42 Z" fill="var(--brand-red)"/>
    <path class="bottom-accent" d="M880,410 L1390,368 L1390,410 Z" fill="var(--brand-red)"/>
    <path class="curve-accent" d="M440,0 C545,120 535,300 480,410 L505,410 C565,300 565,120 470,30 Z" fill="var(--brand-red)"/>
    <path class="panel-grey" d="M0,0 L440,0 C540,120 530,300 480,410 L0,410 Z" fill="var(--panel-grey)"/>

    <g class="brand">
      <circle cx="70" cy="150" r="16" fill="var(--brand-red)"/>
      <text class="brand-name" x="100" y="182" font-size="90">TINTORA</text>
    </g>
    <g class="brand-line">
      <rect x="58" y="331" width="22" height="22" fill="var(--brand-red)"/>
      <text class="tagline" x="92" y="350" font-size="19">Tintora Scheibentönung München</text>
    </g>

    <g class="message" transform="rotate(-2 1010 230)">
      <text class="headline" x="1010" y="135" font-size="112" text-anchor="middle" textLength="690" lengthAdjust="spacingAndGlyphs">PROFESSIONELLE</text>
      <text class="headline" x="1020" y="258" font-size="112" text-anchor="middle" textLength="690" lengthAdjust="spacingAndGlyphs">SCEIBENTÖNUNG</text>
      <line x1="645" y1="284" x2="870" y2="284" stroke="var(--brand-red)" stroke-width="4"/>
      <line x1="1075" y1="284" x2="1300" y2="284" stroke="var(--brand-red)" stroke-width="4"/>
      <text class="website" x="972" y="292" font-size="26" text-anchor="middle">www.tintora.de</text>
      <rect class="phone-pill" x="705" y="302" width="535" height="72" rx="12" fill="var(--brand-red)"/>
      <text class="phone" x="972" y="356" font-size="48" text-anchor="middle">0151 - 48230 - 916</text>
      <text class="address" x="972" y="398" font-size="19" text-anchor="middle">Lindenweg 7, 85540 Haar</text>
    </g>
  </svg>
</main>
</body>
</html>
```